Business card design needed

I need a business card for my private practice. I would like to see the designs that use bright blue and white. I would like to see similar designs as to the card below:
http://blog.tagmerix.com/2009/designing-a-business-card-with-tm-kp517-template.html
I would like to see the back of the card have room for appointment times. Thank you.

Industry/Entity Type
Business
Contact Information for Business Card
Harbour Mindwell & Guidance Services
Fiona Dalgety B.Psychology
Registered Psychologist
Building C, Level 3, 14 Mereton Crescent, Canberra, ACT 2601
T: (02) 6173 8251
F: (02) 6173 8290
info@harbourmindwell.com.au
www.harbourmindwell.com.au

```html
<!DOCTYPE html>
<html lang="en">
<head>
<meta charset="utf-8">
<title>Harbour Mindwell &amp; Guidance Services – Business Card</title>
<link rel="stylesheet" href="https://fonts.googleapis.com/css2?family=EB+Garamond:wght@400;500;600&display=swap">
<style>
  :root {
    --backdrop: #d1d2d4;
    --card-white: #ffffff;
    --pale-blue: #b3e5f7;
    --sky-blue: #8fd5f7;
    --brand-blue: #1ba6e1;
    --ink: #1e1e1e;
    --muted: #6b6b6b;
    --shadow: rgba(0, 0, 0, 0.45);
  }
  * { box-sizing: border-box; margin: 0; padding: 0; }
  html, body { width: 792px; height: 1200px; overflow: hidden; }
  body {
    background: var(--backdrop);
    font-family: "EB Garamond", "Garamond", serif;
    color: var(--ink);
    position: relative;
  }
  .card {
    position: absolute;
    width: 736px;
    height: 398px;
    overflow: hidden;
    box-shadow: 8px 8px 10px var(--shadow);
  }
  .card--front { left: 42px; top: 130px; background: var(--card-white); }
  .card--back  { left: 44px; top: 651px; width: 738px; background: var(--sky-blue); }

  .brand-panel {
    position: absolute;
    left: 0; top: 0;
    width: 341px; height: 100%;
  }
  .card--front .brand-panel { background: var(--pale-blue); }
  .card--back  .brand-panel { background: var(--card-white); }

  .practice-name {
    position: absolute;
    left: 104px; top: 164px;
    font-weight: 600;
    font-size: 19px;
    line-height: 21px;
    letter-spacing: 0.2px;
    text-transform: uppercase;
    color: var(--brand-blue);
  }

  .details {
    position: absolute;
    left: 368px; top: 30px;
    right: 20px;
  }
  .person-name { font-size: 29px; font-weight: 600; line-height: 34px; }
  .person-role { font-size: 20px; line-height: 24px; color: var(--muted); }
  .card--back .person-role { color: var(--ink); }

  .address {
    margin-top: 68px;
    font-size: 20px;
    line-height: 28px;
    font-style: normal;
  }
  .contact-list { list-style: none; margin-top: 4px; }
  .contact-list li {
    font-size: 20px;
    line-height: 32px;
    display: flex;
    align-items: baseline;
  }
  .contact-label {
    width: 34px;
    font-size: 12px;
    letter-spacing: 0.5px;
  }
</style>
</head>
<body>

  <section class="card card--front" aria-label="Business card front">
    <div class="brand-panel"></div>
    <p class="practice-name">Harbour Mindwell<br>&amp; Guidance Services</p>
    <div class="details">
      <h1 class="person-name">Fiona Dalgety</h1>
      <p class="person-role">Registered Psychologist</p>
      <address class="address">Building C, Level 3,<br>14 Mereton Crescent,<br>Canberra, ACT 2601</address>
      <ul class="contact-list">
        <li><span class="contact-label">T</span>(02) 6173 8251</li>
        <li><span class="contact-label">F</span>(02) 6173 8290</li>
        <li><span class="contact-label">E</span>info@harbourmindwell.com.au</li>
        <li><span class="contact-label">W</span>www.harbourmindwell.com.au</li>
      </ul>
    </div>
  </section>

  <section class="card card--back" aria-label="Business card alternate colourway">
    <div class="brand-panel"></div>
    <p class="practice-name">Harbour Mindwell<br>&amp; Guidance Services</p>
    <div class="details">
      <h2 class="person-name">Fiona Dalgety</h2>
      <p class="person-role">Registered Psychologist</p>
      <address class="address">Building C, Level 3,<br>14 Mereton Crescent,<br>Canberra, ACT 2601</address>
      <ul class="contact-list">
        <li><span class="contact-label">T</span>(02) 6173 8251</li>
        <li><span class="contact-label">F</span>(02) 6173 8290</li>
        <li><span class="contact-label">E</span>info@harbourmindwell.com.au</li>
        <li><span class="contact-label">W</span>www.harbourmindwell.com.au</li>
      </ul>
    </div>
  </section>

</body>
</html>
```